Halt and Thicken New Branding Stationary Set - updated Oct 30th 2017

Updated on 30th Oct 2017 as we now need a whole folder design instead of a folder cover. We have thought out exactly what should be on it so it wont be hard. We are happy for this to be completed only by the winning designer if you like. And also we are guaranteeing this project now. Thanks!

We just got our new logo and now we would like a stationary set so we can brand our company communications. The items we need designed are:
Business cards
Letterhead
Appointment confirmation cards
Folder - switched from folder cover. Note that if you don't wish to do this unless you are selected as the winner this is fine.

1. Business cards - for 5 employees, final names will be given once the winner is selected, but you can use this one as the sample:
Lucinda Prieto
Hair Regrowth Expert
Halt and Thicken
7127 Marbury Ave, Suite 500
Kestrel Park CA 90877
lucinda@gavinthorpemd.example
(555) 238-9016

2. Letterhead 8.5" x 11.0" vertical
Halt and Thicken
Kestrel Park CA 90877
office@haltandthicken.example
(555) 238-9016

3. Appointment Confirmation cards - business card size
Halt and Thicken
Kestrel Park CA 90877
Appointment For:
Date:
Time:
If you are unable to make your appointment, please contact us to reschedule at:
(555) 238-9016
info@gavinthorpemd.example

*UPDATED*
4. Folder 9" x 12 " vertical with double pocket
We would like the infinity image from the logo made really big so the left side is on the back and the right side with the + sign is on the front and its takes up the maximum room on the folder.
On the front below the half logo it should say "A Biochemical Revolution..."
On the inside we would also like to have the infinity sign from the logo but faded and half on the left pocket half on the right.
On left inside pocket it should say (this will be partically written on top of the logo):
Gavin Thorpe MD
Precision Medicine
Halt and Thicken Hair
On the Right inside pocket it should say the following:
Because the Enemy of BETTER Health is Good Health
BETTER Ingredients
BETTER Recipe
BETTER Medicine
On the back below the logo on the bottom should be the contact information.
I attached a picture of our drawing of what we want for this to make it easier.

Here is our website to give you an idea of our branding: http://www.haltandthicken.example/

We are the only true cure for hair loss and need to look professional and highest quality and beyond reproach from an ethical standpoint. We are a medical clinic so this should be portrayed also.
We cured hair loss by analyzing biochemistry and rebalancing it so that the process reverses and your own hair can grow back naturally.

Business card information:

OK so here is the information for the business cards:

Lucinda Prieto
Hair Regrowth Expert
(555) 238-9016
www.haltandthicken.example

Marisol Quintero
Hair Growth Consultant
(555) 238-9016
marisol@gavinthorpemd.example
www.haltandthicken.example

Glenda Hutchins
CMO/COO
(555) 238-9016
glenda@haltandthicken.example
www.haltandthicken.example

Dr Lou Thorpe
President
(555) 238-9016
info@gavinthorpemd.example
www.haltandthicken.example

Halt and Thicken
Customer Service
(555) 238-9016
info@gavinthorpemd.example
www.haltandthicken.example

Target Market(s)

Men aged 20-24 who care about their appearance, care about their hair and care about the world.

Industry/Entity Type

Medical And Science

Font styles to use
Sans Serif

Colors
00a990
ffffff
9d9d9d
333333

Requirements
Must have
• Must use the logo and our brand colors from the logo in all designs.
• The pantone colors are:
• Green: #4ca26f
• Light Grey: #999999
• The design should be symmetrical and balanced.
Nice to have
• It should look reasonably masculine.
Should not have
• Do not include any red in the design.

```html
<!DOCTYPE html>
<html lang="en">
<head>
<meta charset="utf-8">
<title>Halt and Thicken – Appointment Card</title>
<link href="https://fonts.googleapis.com/css2?family=Montserrat:wght@700&family=Open+Sans:wght@400;600&display=swap" rel="stylesheet">
<style>
  :root {
    --green: #4ca26f;
    --grey: #999999;
    --ink: #333333;
    --rule: #555555;
    --paper: #ffffff;
    --backdrop: #1c1c1c;
  }
  * { box-sizing: border-box; margin: 0; padding: 0; }
  html, body { width: 1200px; height: 1200px; overflow: hidden; }
  body {
    background: var(--backdrop);
    font-family: "Open Sans", Arial, sans-serif;
    color: var(--ink);
    position: relative;
  }
  .card {
    position: absolute;
    left: 150px;
    width: 900px;
    height: 515px;
    background: var(--paper);
    overflow: hidden;
  }
  .card--appointment { top: 60px; }
  .card--front { top: 625px; }

  .card__band {
    position: absolute;
    left: 0; right: 0; bottom: 0;
    height: 16px;
    display: flex;
  }
  .card__band-green { background: var(--green); }
  .card__band-grey { background: var(--grey); flex: 1; }
  .card--appointment .card__band-green { width: 62%; }
  .card--front .card__band-green { width: 66%; }

  /* Appointment side */
  .appointment__title {
    position: absolute;
    top: 62px; left: 0; right: 0;
    text-align: center;
    font-family: "Montserrat", Arial, sans-serif;
    font-weight: 700;
    font-size: 28px;
    letter-spacing: 1px;
    color: var(--green);
  }
  .appointment__fields {
    position: absolute;
    left: 70px; right: 70px; top: 150px;
  }
  .field {
    display: flex;
    align-items: flex-end;
    height: 60px;
    font-size: 22px;
  }
  .field__label { width: 80px; padding-bottom: 2px; }
  .field__line { flex: 1; border-bottom: 1.5px solid var(--rule); height: 1px; margin-bottom: 8px; }

  .appointment__notice {
    position: absolute;
    left: 40px; right: 40px; top: 375px;
    text-align: center;
    font-size: 20px;
  }
  .appointment__contacts {
    position: absolute;
    left: 0; right: 0; top: 420px;
    display: flex;
    justify-content: center;
    gap: 40px;
    font-size: 20px;
  }
  .contact { display: flex; align-items: center; gap: 10px; }
  .contact svg { fill: var(--green); }

  /* Front side */
  .brand {
    position: absolute;
    top: 120px; left: 0; right: 0;
    display: flex;
    justify-content: center;
    align-items: center;
    gap: 18px;
  }
  .brand__dot {
    width: 26px; height: 26px;
    border-radius: 50%;
    background: var(--green);
  }
  .brand__name {
    font-family: "Open Sans", Arial, sans-serif;
    font-weight: 600;
    font-size: 50px;
    letter-spacing: 1px;
    color: var(--green);
    text-transform: uppercase;
  }
  .address {
    position: absolute;
    top: 290px; left: 430px;
    width: 420px;
    text-align: center;
    font-size: 21px;
    line-height: 1.35;
  }
  .address__pin { fill: var(--green); display: block; margin: 0 auto 8px; }
</style>
</head>
<body>

<section class="card card--appointment">
  <h2 class="appointment__title">APPOINTMENT DATE</h2>
  <div class="appointment__fields">
    <div class="field"><span class="field__label">For:</span><span class="field__line"></span></div>
    <div class="field"><span class="field__label">Time:</span><span class="field__line"></span></div>
    <div class="field"><span class="field__label">Date:</span><span class="field__line"></span></div>
  </div>
  <p class="appointment__notice">If you are unable to make your appointment, please contact us to reschedule at</p>
  <div class="appointment__contacts">
    <span class="contact">
      <svg width="18" height="18" viewBox="0 0 24 24" aria-hidden="true"><path d="M6.6 10.8a15.1 15.1 0 0 0 6.6 6.6l2.2-2.2c.3-.3.7-.4 1-.2 1.1.4 2.3.6 3.6.6.6 0 1 .4 1 1V20c0 .6-.4 1-1 1A17 17 0 0 1 3 4c0-.6.4-1 1-1h3.5c.6 0 1 .4 1 1 0 1.3.2 2.5.6 3.6.1.3 0 .7-.2 1z"/></svg>
      (555) 238-9016
    </span>
    <span class="contact">
      <svg width="20" height="16" viewBox="0 0 24 18" aria-hidden="true"><path d="M0 0h24v18H0z M2 2v1l10 7 10-7V2z" fill-rule="evenodd"/></svg>
      info@gavinthorpemd.example
    </span>
  </div>
  <div class="card__band"><span class="card__band-green"></span><span class="card__band-grey"></span></div>
</section>

<section class="card card--front">
  <div class="brand">
    <span class="brand__dot"></span>
    <span class="brand__name">Halt and Thicken</span>
  </div>
  <address class="address" style="font-style:normal">
    <svg class="address__pin" width="26" height="34" viewBox="0 0 24 32" aria-hidden="true"><path d="M12 0a12 12 0 0 0-12 12c0 9 12 20 12 20s12-11 12-20A12 12 0 0 0 12 0zm0 17a5 5 0 1 1 0-10 5 5 0 0 1 0 10z"/></svg>
    Halt and Thicken<br>
    7127 Marbury Ave, Suite 500<br>
    Kestrel Park CA 90877
  </address>
  <div class="card__band"><span class="card__band-green"></span><span class="card__band-grey"></span></div>
</section>

</body>
</html>
```